Flyer-Design
Zielgruppe
Clown Zauberer Ballonkünstler
Zirkus
Unterhaltung für Kinder und Familien Bei Geburtstag, Hochzeit, Tag der offenen Türe
Bitte beachten - DIN Lang 210 mal 105
Aufgabenstellung
Ich brauche einen Flyer der Familien anspricht. Es soll ein Eycatcher sein, der klarmacht, dass hier gute und professionelle Unterhaltung buchbar ist.
Bitte das Logo einbinden - bei den Fotos lasse ich mal freie Hand.
1. Seite - Vorderseite
Überschrift: Clown Pimbo - Spaßmacher der Herzen
Text:
Zirkus Kunterlust:
Hereinspaziert – der Zirkus ist da! Die Kinderund Verwachsenen sind ganz aufgeregt, wenn Pimbo der Zirkusclown das Geschehen erobert. Wenn der große Koffer aufgestellt wird und Pimbo mit seiner Flüstertüte Werbung macht... dann geht es los!
Angelehnt an den klassischen Zirkus und dem modernen Clown, erzeugt Pimbo der Zauberer, Jongleur und Clown ein Bild des klassischen Zirkus; mit einer kleinen und feinen Begrenzung: Ein Clown und ein Koffer reichen, um das Flair eines Zeltes, eine Zirkus-Show und die lachenden Kinderaugen zu erzeugen.
2. Seite - Rückseite:
Ballonkünstler
Erleben Sie wie Pimbo der Ballonkünstler Wunderwerke der Ballonkunst individuell von Zauberhand formt.
Der Ballonkünstler knotet unglaubliche Figuren direkt vor Ihren Augen.
Ein Ballonspektakel mit viel Witz, Charme und Interaktion!
Pimbo der Clown spielt auf der Bühne, auf der Gass, im Wohnzimmer, Garten, in Kitas, Schulen, Firmen, Nachbarschaftszentren - einfach überall.
Kontakt:
Clown Pimbo
www.clown-pimbo-beispiel.de
Tel.: 0176/5081729

```html
<!DOCTYPE html>
<html lang="de">
<head>
<meta charset="utf-8">
<title>Clown Pimbo – Spaßmacher der Herzen</title>
<link href="https://fonts.googleapis.com/css2?family=Montserrat:wght@300;400;500&display=swap" rel="stylesheet">
<style>
  :root {
    --panel-blue: #b5d3e7;
    --title-red: #e8100f;
    --text-white: #ffffff;
    --photo-light: #f1f1f1;
    --photo-mid: #e2e2e2;
    --photo-accent: #d9473a;
  }
  html, body {
    margin: 0;
    padding: 0;
    overflow: hidden;
  }
  body {
    width: 1200px;
    height: 600px;
    font-family: "Montserrat", sans-serif;
  }
  .flyer {
    position: relative;
    width: 1200px;
    height: 600px;
    overflow: hidden;
    background: #ffffff;
  }
  .flyer__backdrop {
    position: absolute;
    inset: 0;
  }
  .flyer__title {
    position: absolute;
    left: 0;
    top: 74px;
    width: 792px;
    margin: 0;
    text-align: center;
    color: var(--title-red);
    font-weight: 400;
    font-size: 47px;
    line-height: 55px;
    letter-spacing: 0.5px;
  }
  .flyer__body {
    position: absolute;
    left: 37px;
    top: 253px;
    width: 687px;
    color: var(--text-white);
    font-weight: 300;
    font-size: 20.5px;
    line-height: 24.2px;
    text-align: justify;
  }
  .flyer__body h2 {
    margin: 0;
    font-size: 21.5px;
    font-weight: 500;
    line-height: 25px;
  }
  .flyer__body p {
    margin: 0 0 24.2px;
  }
  .brand-mark {
    position: absolute;
    left: 1042px;
    top: 18px;
    width: 123px;
    height: 128px;
    background: var(--panel-blue);
    display: flex;
    align-items: center;
    justify-content: center;
    color: var(--title-red);
    font-weight: 500;
    font-size: 28px;
  }
</style>
</head>
<body>
  <div class="flyer">
    <svg class="flyer__backdrop" width="1200" height="600" viewBox="0 0 1200 600" xmlns="http://www.w3.org/2000/svg">
      <defs>
        <linearGradient id="photoTone" x1="0" y1="0" x2="0" y2="1">
          <stop offset="0" stop-color="var(--photo-light)"/>
          <stop offset="0.55" stop-color="#e9e9e9"/>
          <stop offset="1" stop-color="var(--photo-mid)"/>
        </linearGradient>
        <radialGradient id="performerTone" cx="0.6" cy="0.6" r="0.55">
          <stop offset="0" stop-color="var(--photo-accent)" stop-opacity="0.35"/>
          <stop offset="1" stop-color="var(--photo-accent)" stop-opacity="0"/>
        </radialGradient>
      </defs>
      <g role="img" aria-label="Foto: Clown im roten Anzug sitzt in einem großen offenen Koffer und lüftet seinen Hut">
        <rect x="700" y="0" width="500" height="600" fill="url(#photoTone)"/>
        <rect x="780" y="120" width="420" height="340" fill="url(#performerTone)"/>
      </g>
      <path class="flyer__panel" d="M0 0 H763 C772 120 786 260 772 400 C764 480 752 550 737 600 H0 Z" fill="var(--panel-blue)"/>
    </svg>

    <h1 class="flyer__title">Clown Pimbo -<br>Spaßmacher der Herzen</h1>

    <div class="flyer__body">
      <h2>Zirkus Kunterlust:</h2>
      <p>Hereinspaziert – der Zirkus ist da! Die Kinderund Verwachsenen sind ganz aufgeregt, wenn Pimbo der Zirkusclown das Geschehen erobert. Wenn der große Koffer aufgestellt wird und Pimbo mit seiner Flüstertüte Werbung macht... dann geht es los!</p>
      <p>Angelehnt an den klassischen Zirkus und dem modernen Clown, erzeugt Pimbo der Zauberer, Jongleur und Clown ein Bild des klassi&shy;schen Zirkus; mit einer kleinen und feinen Begrenzung: Ein Clown und ein Koffer reichen, um das Flair eines Zeltes, eine Zirkus-Show und die lachenden Kinderaugen zu erzeugen.</p>
    </div>

    <div class="brand-mark">Pimbo</div>
  </div>
</body>
</html>
```